IT services company requires Letterhead design

We need a professional letterhead designed to be used for general correspondence with customers, quotes, invoices etc. We are a new IT services company specialising in computer servicing and repairs and mobile and tablet repairs. Attached are templates that my printing company have supplied, my logos, an interpretation of our website for you to get a feel of the company. Details to be included on the letterhead are

Company Number – 4830517
VAT Number - 581736294
Registered Address – 14-16 Brambury Lane, London, E9 3PL

Phone – 01843 572236
Email – sales@quorvant.com
Web – www.quorvant.com

I would prefer for the top of the letterhead to just have the company logo on a white background and the rest of the details on the bottom of the letterhead but I am open to design ideas.

Thanks

```html
<!DOCTYPE html>
<html lang="en">
<head>
<meta charset="utf-8">
<title>Quorvant Letterhead</title>
<link rel="stylesheet" href="https://fonts.googleapis.com/css2?family=Nunito:wght@800;900&display=swap">
<style>
  :root {
    --page-bg: #ffffff;
    --canvas-bg: #ffffff;
    --frame: #c4c4c4;
    --accent-orange: #fbb040;
    --ink-navy: #2e3192;
    --logo-blue: #1e9ad6;
    --watermark: #ececec;
  }
  * { margin: 0; padding: 0; box-sizing: border-box; }
  html, body {
    width: 1200px;
    height: 1101px;
    overflow: hidden;
    background: var(--canvas-bg);
  }
  .letterhead {
    position: absolute;
    left: 164px;
    top: 22px;
    width: 817px;
    height: 1056px;
    background: var(--page-bg);
    border: 1px solid var(--frame);
    font-family: "Nunito", Arial, sans-serif;
  }
  .header-rule {
    position: absolute;
    left: 0;
    top: 64px;
    width: 729px;
    height: 8px;
    background: var(--accent-orange);
  }
  .brand {
    position: absolute;
    right: 14px;
    top: 26px;
    display: flex;
    align-items: center;
    gap: 6px;
  }
  .brand-square {
    width: 12px;
    height: 12px;
    background: var(--logo-blue);
  }
  .brand-name {
    font-weight: 900;
    font-size: 22px;
    color: var(--logo-blue);
    letter-spacing: -0.3px;
  }
  .watermark {
    position: absolute;
    left: 130px;
    top: 310px;
    width: 556px;
    height: 460px;
    display: flex;
    align-items: center;
    justify-content: center;
    gap: 22px;
  }
  .watermark-square {
    width: 60px;
    height: 60px;
    background: var(--watermark);
  }
  .watermark-name {
    font-weight: 900;
    font-size: 104px;
    color: var(--watermark);
    letter-spacing: -2px;
  }
  .footer-band {
    position: absolute;
    left: 0;
    bottom: 0;
    width: 100%;
    height: 52px;
    background: var(--accent-orange);
    display: flex;
    flex-direction: column;
    justify-content: center;
    gap: 2px;
    padding: 0 14px;
    font-weight: 800;
    font-size: 12.5px;
    line-height: 1.3;
    color: var(--ink-navy);
    white-space: nowrap;
  }
  .footer-row {
    display: flex;
    align-items: center;
  }
  .footer-divider {
    display: inline-block;
    width: 1.5px;
    height: 13px;
    background: var(--ink-navy);
    margin: 0 9px;
  }
</style>
</head>
<body>
  <main class="letterhead">
    <div class="header-rule"></div>
    <div class="brand">
      <span class="brand-square"></span>
      <span class="brand-name">Quorvant</span>
    </div>

    <div class="watermark" aria-hidden="true">
      <span class="watermark-square"></span>
      <span class="watermark-name">Quorvant</span>
    </div>

    <footer class="footer-band">
      <div class="footer-row footer-registration">
        <span class="footer-company-no">Company No : 4830517</span>
        <span class="footer-divider"></span>
        <span class="footer-vat-no">VAT No : 581736294</span>
      </div>
      <div class="footer-row footer-contact">
        <span class="footer-address">RA : 14-16 Brambury Lane, London, E9 3PL,&nbsp; Phone :&nbsp; 01843 572236</span>
        <span class="footer-divider"></span>
        <span class="footer-online">E-mail : sales@quorvant.com, Web : www.quorvant.com</span>
      </div>
    </footer>
  </main>
</body>
</html>
```